Etiketten für Hersteller und Vertreiber von Tierpflegeprodukten
Zielgruppe
hersteller und vertreiber von tierpflegeprodukten, Absatz hauptsächlich über das Internet (Online-Shop), Angebot reicht von hochwertigen Bio-Artikeln, über konventionelle Pflegeprodukte bis hin zu spezial Produkten wie für Hundesalons oder hypoallergene Pflegeprodukte
Ziel: weit gefächert, alle Tierbesitzer von Hunden/Katzen/Pferden und weiteren Kleintieren
kleine Gebinde von 100ml oder 200ml über 500ml bis zu 2l / Professionelle Produkte: 5l und 20l
Angedacht sind drei Sprachen: französisch vordergründig, zudem klein englisch und spanisch (Texte sind vorhanden)
Aufgabenstellung
gerade die Etiketten von den kleinen Gebinden (100ml) betragen nur 70x110 (in mm), der Hauptteil (Shampoo in 200ml) tragen eine Etikette der Größe 100x150, alles andere bekommt 120x150
auf dieser Fläche müß der Name 'VELUSIRANT' 'bio' deutlich zu sehen sein, Achtung, es sind Rundflaschen, desweiteren sollte eventuell der Wirkstoff (zB. Granatapfel) zu sehen sein (Abbildungen von jedem Wirkstoff/Pflanzenrohstoff sind exklusiv vorhanden)
Natürlich muss die Produktkategorie erscheinen (Shampoo / Spülung / Ohrenreiniger / Pfotencreme etc)
Auf der Rückseite kommt der Text zu dem Pflegeprodukt in den drei Sprachen (vorhanden) sowie weitere obligatorische Angaben und der BarCode
Im Onlineshop sind natürlich Abbildungen der Flaschen zu sehen: hier muss der Kunde es 'einladend / modern / bio / pflegend / exclusiv' finden
Als Datei füge ich 'Vorstellungen' über den Gebrauch der Marke ein / unsere 'Versuche' die nicht uns zufriedenstellten / ein Bild von der Rundflsche mit den entsprechenden 'Versuchen'
Der Name atelier sol montevu kann vernachlässigt werden, er ist nicht wichtig. Wichtig ist wirklich die Frontseite

```html
<!DOCTYPE html>
<html lang="fr">
<head>
<meta charset="utf-8">
<title>VELUSIRANT bio – Shampooings</title>
<link href="https://fonts.googleapis.com/css2?family=Cabin:wght@400;500;600&family=Cabin+Condensed:wght@400;500&family=Lora:ital@1&display=swap" rel="stylesheet">
<style>
  :root {
    --page: #ffffff;
    --label-top: #f2f3f4;
    --label-mid: #e6e8ea;
    --ink: #2b2b2b;
    --brand: #3a3a3a;
    --band-text: #2f3a34;
    --cat-band: #8fa98f;
    --cat-bio: #8fb39e;
    --cat-sun: #ece3a6;
    --cat-plant: #d9d7a2;
    --dog-band: #93abb6;
    --dog-bio: #8fb1bc;
    --dog-sun: #d5e2dc;
    --dog-plant: #a9c08d;
    --horse-band: #df7d73;
    --horse-bio: #e1706a;
    --horse-sun: #ecc07a;
    --horse-plant: #b8a17a;
    --rule: rgba(255,255,255,0.55);
  }
  * { box-sizing: border-box; margin: 0; padding: 0; }
  html, body { width: 1200px; height: 848px; overflow: hidden; background: var(--page); }
  .range {
    width: 1200px; height: 848px;
    display: flex; justify-content: center; align-items: center; gap: 60px;
  }
  .label {
    width: 300px; height: 560px; position: relative; overflow: hidden;
    background: linear-gradient(90deg, var(--label-mid), var(--label-top) 45%, var(--label-mid));
    font-family: "Cabin", sans-serif; color: var(--ink);
  }
  .brand {
    position: absolute; top: 34px; left: 0; right: 0; text-align: center;
    font-family: "Cabin", sans-serif; font-weight: 500; font-size: 27px;
    letter-spacing: 3px; color: var(--brand);
  }
  .plant {
    position: absolute; top: 90px; left: 20px; width: 260px; height: 200px;
    border-radius: 50%;
  }
  .bio {
    position: absolute; top: 82px; left: 50%; transform: translateX(-50%);
    width: 80px; height: 80px; border-radius: 50%;
    display: flex; align-items: center; justify-content: center;
    font-family: "Lora", serif; font-style: italic; font-size: 38px; color: #fff;
  }
  .product { position: absolute; top: 298px; left: 0; right: 0; text-align: center; }
  .product-name {
    display: inline-block; font-weight: 600; font-size: 24px; letter-spacing: 1.5px;
    padding: 0 4px 3px; border-bottom: 1.5px solid var(--accent);
  }
  .product-active { font-size: 19px; margin-top: 5px; }
  .band {
    position: absolute; left: 0; right: 0; top: 360px; bottom: 0;
    background: var(--band);
  }
  .band-rule { position: absolute; left: 10px; right: 10px; top: 82px; height: 1px; background: var(--rule); }
  .sun {
    position: absolute; left: 50%; top: 30px; transform: translateX(-50%);
    width: 116px; height: 116px; border-radius: 50%;
  }
  .claim {
    position: absolute; width: 82px; text-align: center;
    font-family: "Cabin Condensed", sans-serif; font-size: 15.5px; line-height: 1.2;
    color: var(--band-text);
  }
  .claim.left { left: 8px; }
  .claim.right { right: 6px; }
  .claim.benefit { top: 32px; }
  .claim.active { top: 90px; }
  .category {
    position: absolute; left: 0; right: 0; bottom: 20px; text-align: center;
    font-size: 11px; line-height: 1.35; color: var(--band-text);
  }
  .category .small { font-size: 9.5px; white-space: nowrap; }
  .cat { --band: var(--cat-band); --accent: var(--cat-band); }
  .dog { --band: var(--dog-band); --accent: var(--dog-band); }
  .horse { --band: var(--horse-band); --accent: var(--horse-band); }
</style>
</head>
<body>
<main class="range">

  <article class="label cat">
    <div class="brand">VELUSIRANT</div>
    <div class="plant" role="img" aria-label="Photo de fleurs et feuilles de henné" style="background: radial-gradient(ellipse at center, var(--cat-plant) 0%, #b9cf9a 45%, rgba(242,243,244,0) 72%);"></div>
    <div class="bio" style="background: var(--cat-bio);">bio</div>
    <div class="product">
      <div class="product-name">BRILLANCE</div>
      <div class="product-active">Hennè neutre</div>
    </div>
    <section class="band">
      <div class="band-rule"></div>
      <div class="sun" role="img" aria-label="Illustration d'un chat noir sur disque clair" style="background: var(--cat-sun);"></div>
      <p class="claim left benefit">for<br>shiny coat</p>
      <p class="claim right benefit">für<br>mehr Glanz</p>
      <p class="claim left active">Neutral<br>Henna</p>
      <p class="claim right active">Neutrales<br>Henna</p>
      <p class="category">Shampooing speciaux pour chat<br><span class="small">Special Care Shampoo for cats | Pflege-Shampoo für Katzen</span></p>
    </section>
  </article>

  <article class="label dog">
    <div class="brand">VELUSIRANT</div>
    <div class="plant" role="img" aria-label="Photo de grande ortie en fleurs" style="background: radial-gradient(ellipse at center, var(--dog-plant) 0%, #9cb882 45%, rgba(242,243,244,0) 72%);"></div>
    <div class="bio" style="background: var(--dog-bio);">bio</div>
    <div class="product">
      <div class="product-name">VOLUMATEUR</div>
      <div class="product-active">Grand Ortie</div>
    </div>
    <section class="band">
      <div class="band-rule"></div>
      <div class="sun" role="img" aria-label="Illustration d'un chien noir assis sur disque clair" style="background: var(--dog-sun);"></div>
      <p class="claim left benefit">for more<br>volume</p>
      <p class="claim right benefit">für mehr<br>Haarvolumen</p>
      <p class="claim left active">Stinging<br>nettle</p>
      <p class="claim right active">Brennnessel</p>
      <p class="category">Shampooing speciaux pour chiens<br><span class="small">Special Care Shampoo for dogs | Pflege-Shampoo für Hunde</span></p>
    </section>
  </article>

  <article class="label horse">
    <div class="brand">VELUSIRANT</div>
    <div class="plant" role="img" aria-label="Photo de noix, feuilles de noyer et thé noir" style="background: radial-gradient(ellipse at center, var(--horse-plant) 0%, #a9c27c 45%, rgba(242,243,244,0) 72%);"></div>
    <div class="bio" style="background: var(--horse-bio);">bio</div>
    <div class="product">
      <div class="product-name">PELAGE NOIR</div>
      <div class="product-active">Noir et Thé noir</div>
    </div>
    <section class="band">
      <div class="band-rule"></div>
      <div class="sun" role="img" aria-label="Illustration d'un cheval noir au galop sur disque doré" style="background: var(--horse-sun);"></div>
      <p class="claim left benefit">for<br>dark coat</p>
      <p class="claim right benefit">für<br>dunkles Fell</p>
      <p class="claim left active">Walnut &amp;<br>black tea</p>
      <p class="claim right active">Walnuss &amp;<br>schwarzer Tee</p>
      <p class="category">Shampooing speciaux pour cheval<br><span class="small">Special Care Shampoo for horses | Pflege-Shampoo für Pferde</span></p>
    </section>
  </article>

</main>
</body>
</html>
```